Powerpoint master slide deck for power point presentation by members of my company

To design a master slide deck for powerpoint presentation for a Orthopaedic Clinic Based in Singapore

```html
<!DOCTYPE html>
<html lang="en">
<head>
<meta charset="utf-8">
<title>Stride Joint Clinic – Presentation Master Deck</title>
<link href="https://fonts.googleapis.com/css2?family=Ubuntu:wght@300;400;500;700&display=swap" rel="stylesheet">
<style>
:root{
  --teal:#5bb7b2;
  --teal-soft:#7cc7c2;
  --teal-dark:#2f7a75;
  --ink:#1f4f4c;
  --text:#4a4a4a;
  --muted:#8a8a8a;
  --rule:#e6e6e6;
  --page:#dcdcdc;
  --white:#ffffff;
}
*{box-sizing:border-box;margin:0;padding:0}
html,body{width:1200px;height:2430px;overflow:hidden}
body{position:relative;background:var(--page);font-family:"Ubuntu",sans-serif;color:var(--text)}

/* hero */
.hero{position:absolute;left:0;top:0;width:1200px;height:720px;background:linear-gradient(180deg,#eef0f3 0%,#e2e5e9 100%)}
.hero-brand{position:absolute;right:50px;top:56px}
.hero-stage{position:absolute;left:263px;top:160px;transform:scale(1.2);transform-origin:0 0;box-shadow:0 12px 30px rgba(0,0,0,.18)}
.hero-stage .slide{position:relative;left:0;top:0}

/* brand */
.brand{display:flex;align-items:center;gap:6px;font-family:"Ubuntu",sans-serif;font-weight:400;white-space:nowrap}
.brand-square{display:block;background:currentColor}
.brand--hero{color:var(--teal-dark);font-size:26px}
.brand--hero .brand-square{width:26px;height:26px}
.brand--cover{color:var(--white);font-size:15px}
.brand--cover .brand-square{width:16px;height:16px}

/* slide */
.slide{position:absolute;width:562px;height:316px;background:var(--white);overflow:hidden}
.col-a{left:28px}.col-b{left:609px}
.row-1{top:740px}.row-2{top:1075px}.row-3{top:1410px}.row-4{top:1745px}.row-5{top:2079px}
.abs{position:absolute}

/* cover */
.cover-panel{position:absolute;left:10px;top:10px;width:542px;height:281px;background:var(--teal);border-radius:0 0 70px 0}
.cover-curve{position:absolute;right:10px;top:10px;width:220px;height:281px}
.cover-title{position:absolute;left:44px;top:108px;color:var(--white);font-weight:400;font-size:31px;line-height:34px}
.cover-sub{position:absolute;left:45px;top:183px;color:var(--white);font-size:11px;font-weight:300}
.cover-date{position:absolute;left:45px;top:240px;width:91px;height:13px;background:var(--ink);color:var(--white);font-size:6px;line-height:13px;text-align:center}
.cover-copy{position:absolute;left:0;right:0;top:299px;text-align:center;font-size:5.5px;color:var(--muted)}
.cover .brand--cover{position:absolute;left:44px;top:46px}

/* footer */
.foot{position:absolute;left:14px;right:14px;top:286px;height:14px}
.foot-brand{position:absolute;left:0;top:1px;color:var(--muted);font-size:8px;display:flex;align-items:center;gap:3px}
.foot-brand i{display:block;width:8px;height:8px;background:var(--teal)}
.foot-bar{position:absolute;left:90px;right:0;top:2px;height:10px;background:#f1f1f1;font-size:4.6px;color:#777;text-align:right;padding-right:10px;line-height:10px}

/* headings */
.heading{position:absolute;left:0;right:0;top:14px;text-align:center;font-size:22px;color:var(--ink);font-weight:700}
.heading span{color:var(--teal);font-weight:400}
.kicker{font-weight:700;color:var(--ink);font-size:21px;line-height:24px}
.kicker-line{color:var(--teal);font-weight:400;font-size:21px;line-height:25px}

.tiny{font-size:5px;line-height:6px;color:var(--text)}
.tiny-w{font-size:5px;line-height:6px;color:var(--white)}
.label{font-size:9px;color:var(--teal)}
.label-ink{font-size:9px;color:var(--ink)}

/* icon chip */
.chip{position:absolute;width:30px;height:30px;border-radius:50%;background:var(--teal);display:flex;align-items:center;justify-content:center}
.chip--dark{background:var(--ink)}
.chip svg{width:14px;height:14px}
.tile{position:absolute;width:34px;height:34px;border-radius:4px;background:var(--teal);display:flex;align-items:center;justify-content:center}
.tile--dark{background:var(--ink)}
.tile svg{width:16px;height:16px}

/* agenda */
.agenda-item{position:absolute}
.agenda-item .label{margin-bottom:2px}

/* photo */
.photo{position:absolute;left:281px;top:77px;width:281px;height:119px;background:linear-gradient(135deg,#dfe9f2 0%,#b9c9d6 55%,#8ea1b1 100%)}

/* numbered cards */
.num-card{position:absolute;left:285px;width:235px;height:60px;border-radius:6px;background:#f6f6f6;box-shadow:0 2px 4px rgba(0,0,0,.18);display:flex;align-items:center}
.num-card--active{background:var(--teal-dark)}
.num-card b{width:50px;text-align:center;font-weight:400;font-size:28px;color:var(--teal-dark);border-right:1px solid #c9c9c9}
.num-card--active b{color:var(--white);border-color:rgba(255,255,255,.5)}
.num-card p{padding:0 12px;font-size:6.3px;line-height:7.5px;color:var(--text)}
.num-card--active p{color:var(--white)}

/* table */
.data{position:absolute;left:29px;top:81px;width:506px;border-collapse:collapse;font-size:6px;color:#333}
.data th{height:26px;color:var(--white);font-weight:400;font-size:6.5px;line-height:7px}
.data th.h0{background:#4a4a4a;text-align:left;padding-left:4px}
.data th.h1{background:var(--teal)}
.data th.h2{background:var(--teal-dark)}
.data th.h3{background:var(--ink)}
.data th.h4{background:#a8a8a8}
.data td{height:23px;text-align:center;border-bottom:1px solid #ececec}
.data td:first-child{text-align:left;padding-left:4px}
.data tr:nth-child(even) td{background:#f7f7f7}
.col-frame{position:absolute;left:185px;top:77px;width:88px;height:198px;border:1.5px solid var(--teal-dark);border-radius:4px}
</style>
</head>
<body>

<!-- Hero -->
<section class="hero">
  <div class="hero-brand brand brand--hero"><i class="brand-square"></i>Stride Joint Clinic</div>
  <div class="hero-stage">
    <div class="slide cover">
      <div class="cover-panel"></div>
      <div class="brand brand--cover"><i class="brand-square"></i>Stride Joint Clinic</div>
      <h1 class="cover-title">Presentation<br>Title Goes Here</h1>
      <p class="cover-sub">Subtitle of Presentation Goes Here</p>
      <div class="cover-date">November 17, 2022</div>
      <p class="cover-copy">© 2022 Copyright Stride Joint Clinic - All Rights Reserved</p>
    </div>
  </div>
</section>

<!-- 1 Cover -->
<article class="slide cover col-a row-1">
  <div class="cover-panel"></div>
  <div class="brand brand--cover"><i class="brand-square"></i>Stride Joint Clinic</div>
  <h1 class="cover-title">Presentation<br>Title Goes Here</h1>
  <p class="cover-sub">Subtitle of Presentation Goes Here</p>
  <div class="cover-date">November 17, 2022</div>
  <p class="cover-copy">© 2022 Copyright Stride Joint Clinic - All Rights Reserved</p>
</article>

<!-- 2 Cover alt -->
<article class="slide cover col-b row-1">
  <div class="cover-panel"></div>
  <div class="brand brand--cover"><i class="brand-square"></i>Stride Joint Clinic</div>
  <h1 class="cover-title">Presentation<br>Title Goes Here</h1>
  <p class="cover-sub">Subtitle of Presentation Goes Here</p>
  <div class="cover-date">November 17, 2022</div>
  <p class="cover-copy">© 2022 Copyright Stride Joint Clinic - All Rights Reserved</p>
</article>

<!-- 3 Agenda -->
<article class="slide col-a row-2">
  <div class="abs" style="left:44px;top:108px">
    <div class="kicker">ADIPISCING:</div>
    <div class="kicker-line">Elit Vivamus Eu Dui<br>Ex Curabitur</div>
  </div>
  <svg class="abs" style="left:0;top:0" width="562" height="316" viewBox="0 0 562 316">
    <path d="M170 22 A130 125 0 0 1 170 272" fill="none" stroke="#dedede" stroke-width="4"/>
    <g stroke="#5bb7b2" stroke-width="1.2">
      <line x1="240" y1="40" x2="275" y2="40"/>
      <line x1="288" y1="95" x2="320" y2="95"/>
      <line x1="300" y1="147" x2="333" y2="147" stroke="#1f4f4c"/>
      <line x1="288" y1="200" x2="320" y2="200"/>
      <line x1="240" y1="250" x2="275" y2="250"/>
    </g>
    <circle cx="170" cy="22" r="6" fill="#8a8a8a"/>
    <circle cx="170" cy="272" r="6" fill="#8a8a8a"/>
    <circle cx="240" cy="40" r="5" fill="#5bb7b2"/>
    <circle cx="288" cy="95" r="5" fill="#5bb7b2"/>
    <circle cx="300" cy="147" r="5" fill="#1f4f4c"/>
    <circle cx="288" cy="200" r="5" fill="#5bb7b2"/>
    <circle cx="240" cy="250" r="5" fill="#5bb7b2"/>
  </svg>
  <div class="chip" style="left:275px;top:25px"><svg viewBox="0 0 16 16"><rect x="2" y="4" width="12" height="9" rx="1" fill="#fff"/><path d="M8 6v5M5.5 8.5h5" stroke="#5bb7b2" stroke-width="1.6"/></svg></div>
  <div class="agenda-item" style="left:318px;top:30px"><div class="label">Lorem Ipsum Dolor Sit</div><p class="tiny">Nullam sit amet magna non ex bibendum<br>mollis. Nunc vel neque eu augue dignissim.</p></div>
  <div class="chip" style="left:320px;top:80px"><svg viewBox="0 0 16 16"><circle cx="8" cy="8" r="5" fill="none" stroke="#fff" stroke-width="2"/></svg></div>
  <div class="agenda-item" style="left:363px;top:84px"><div class="label">Consectetur Adipiscing Elit</div><p class="tiny">Nullam sit amet magna non ex bibendum<br>mollis. Nunc vel neque eu augue dignissim.</p></div>
  <div class="chip chip--dark" style="left:333px;top:132px"><svg viewBox="0 0 16 16"><path d="M6 2h4M7 2v5l-4 7h10l-4-7V2" fill="none" stroke="#fff" stroke-width="1.4"/></svg></div>
  <div class="agenda-item" style="left:376px;top:137px"><div class="label-ink">Vivamus Eu Dui Ex</div><p class="tiny">Nullam sit amet magna non ex bibendum<br>mollis. Nunc vel neque eu augue dignissim.</p></div>
  <div class="chip" style="left:320px;top:185px"><svg viewBox="0 0 16 16"><rect x="3" y="9" width="2" height="4" fill="#fff"/><rect x="7" y="6" width="2" height="7" fill="#fff"/><rect x="11" y="3" width="2" height="10" fill="#fff"/></svg></div>
  <div class="agenda-item" style="left:363px;top:190px"><div class="label">Curabitur Dapibus</div><p class="tiny">Nullam sit amet magna non ex bibendum<br>mollis. Nunc vel neque eu augue dignissim.</p></div>
  <div class="chip" style="left:275px;top:235px"><svg viewBox="0 0 16 16"><rect x="3" y="4" width="10" height="7" fill="none" stroke="#fff" stroke-width="1.4"/><path d="M1 13h14" stroke="#fff" stroke-width="1.4"/></svg></div>
  <div class="agenda-item" style="left:318px;top:240px"><div class="label">Dignissim Dui, In Molestie</div><p class="tiny">Nullam sit amet magna non ex bibendum<br>mollis. Nunc vel neque eu augue dignissim.</p></div>
  <div class="foot"><span class="foot-brand"><i></i>Stride Joint</span><div class="foot-bar">© 2022 Copyright Stride Joint Clinic - All Rights Reserved &nbsp;|&nbsp; 3</div></div>
</article>

<!-- 4 Text + photo -->
<article class="slide col-b row-2">
  <h2 class="heading">Heading <span>Goes Here</span></h2>
  <div class="abs" style="left:0;top:77px;width:281px;height:119px;background:var(--teal)"></div>
  <div class="photo" role="img" aria-label="Photo of a doctor writing notes beside a laptop"></div>
  <div class="chip chip--dark" style="left:22px;top:94px;background:#fff"><svg viewBox="0 0 16 16"><circle cx="8" cy="6" r="3" fill="#5bb7b2"/><path d="M3 14c0-3 2-5 5-5s5 2 5 5z" fill="#5bb7b2"/></svg></div>
  <div class="abs" style="left:75px;top:92px;width:190px"><div style="font-size:8px;color:#fff;margin-bottom:3px">Elit Vivamus Eu Dui Ex Curabitur</div><p class="tiny-w">Lorem ipsum dolor sit amet, consectetur adipiscing elit. Vivamus eu dui ex. Curabitur dapibus dignissim dui, in molestie metus feugiat sed. Praesent aliquet lorem ex.</p></div>
  <div class="chip" style="left:22px;top:145px;background:#fff"><svg viewBox="0 0 16 16"><rect x="2" y="4" width="12" height="9" rx="1" fill="#5bb7b2"/><path d="M8 6v5M5.5 8.5h5" stroke="#fff" stroke-width="1.6"/></svg></div>
  <div class="abs" style="left:75px;top:143px;width:190px"><div style="font-size:8px;color:#fff;margin-bottom:3px">Donec risus orci, gravida sit</div><p class="tiny-w">Lorem ipsum dolor sit amet, consectetur adipiscing elit. Vivamus eu dui ex. Curabitur dapibus dignissim dui, in molestie metus feugiat sed. Praesent aliquet lorem ex.</p></div>
  <div class="abs" style="left:27px;top:208px;width:228px"><div class="label-ink" style="margin-bottom:5px">Elit Vivamus Eu Dui Ex Curabitur</div><p class="tiny">Lorem ipsum dolor sit amet, consectetur adipiscing elit. Vivamus eu dui ex. Curabitur dapibus dignissim dui, in molestie metus feugiat sed. Praesent aliquet lorem ex, eu dapibus odio varius at. Duis eget tellus porta, consequat lacus vitae, venenatis dolor. Nulla facilisi. In et sollicitudin lacus. Donec risus orci, gravida sit amet risus vehicula.</p></div>
  <div class="abs" style="left:300px;top:208px;width:232px"><div class="label-ink" style="margin-bottom:5px">Donec risus orci, gravida sit</div><p class="tiny">Lorem ipsum dolor sit amet, consectetur adipiscing elit. Vivamus eu dui ex. Curabitur dapibus dignissim dui, in molestie metus feugiat sed. Praesent aliquet lorem ex, eu dapibus odio varius at. Duis eget tellus porta, consequat lacus vitae, venenatis dolor. Nulla facilisi. In et sollicitudin lacus. Donec risus orci, gravida sit amet risus vehicula.</p></div>
  <div class="foot"><span class="foot-brand"><i></i>Stride Joint</span><div class="foot-bar">© 2022 Copyright Stride Joint Clinic - All Rights Reserved &nbsp;|&nbsp; 4</div></div>
</article>

<!-- 5 Feature grid -->
<article class="slide col-a row-3">
  <div class="abs" style="left:0;top:0;width:201px;height:189px;background:var(--teal);border-radius:0 0 40px 0"></div>
  <h3 class="abs" style="left:44px;top:40px;font-weight:400;font-size:21px;line-height:25px;color:var(--ink)">Elit Vivamus<br>Eu Dui Ex<br>Curabitur</h3>
  <p class="abs" style="left:44px;top:130px;width:140px;font-size:6.5px;line-height:7.5px;color:#fff">Lorem ipsum dolor sit amet, consectetur adipiscing elit. Vivamus eu dui ex. Curabitur dapibus dignissim dui, in dapibus odio.</p>

  <div class="tile" style="left:223px;top:48px"><svg viewBox="0 0 16 16"><circle cx="7" cy="7" r="4" fill="none" stroke="#fff" stroke-width="1.8"/><path d="M10 10l4 4" stroke="#fff" stroke-width="2"/></svg></div>
  <div class="abs" style="left:266px;top:46px;width:110px"><div class="label" style="font-size:8px">Vivamus Eu Dui Ex</div><p class="tiny">Praesent aliquet lorem ex, eu dapibus odio varius at. Duis eget tellus porta, consequat lacus vitae.</p></div>
  <div class="tile tile--dark" style="left:388px;top:48px"><svg viewBox="0 0 16 16"><rect x="4" y="2" width="8" height="12" rx="1" fill="#fff"/></svg></div>
  <div class="abs" style="left:431px;top:46px;width:110px"><div class="label-ink" style="font-size:8px">Nulla Facilisi In Et</div><p class="tiny">Praesent aliquet lorem ex, eu dapibus odio varius at. Duis eget tellus porta, consequat lacus vitae.</p></div>

  <div class="tile tile--dark" style="left:223px;top:123px"><svg viewBox="0 0 16 16"><text x="8" y="13" text-anchor="middle" font-size="13" font-weight="700" fill="#fff" font-family="Ubuntu, sans-serif">$</text></svg></div>
  <div class="abs" style="left:266px;top:121px;width:110px"><div class="label-ink" style="font-size:8px">Gravida Sit Amet Risus</div><p class="tiny">Praesent aliquet lorem ex, eu dapibus odio varius at. Duis eget tellus porta, consequat lacus vitae.</p></div>
  <div class="tile" style="left:388px;top:123px"><svg viewBox="0 0 16 16"><circle cx="5" cy="6" r="2" fill="#fff"/><circle cx="11" cy="6" r="2" fill="#fff"/><path d="M1 13c0-2 2-4 4-4s4 2 4 4zM7 13c0-2 2-4 4-4s4 2 4 4z" fill="#fff"/></svg></div>
  <div class="abs" style="left:431px;top:121px;width:110px"><div class="label" style="font-size:8px">Vivamus Eu Dui Ex</div><p class="tiny">Praesent aliquet lorem ex, eu dapibus odio varius at. Duis eget tellus porta, consequat lacus vitae.</p></div>

  <div class="tile" style="left:223px;top:198px"><svg viewBox="0 0 16 16"><circle cx="8" cy="8" r="6" fill="none" stroke="#fff" stroke-width="1.6"/><path d="M8 4v4h3" fill="none" stroke="#fff" stroke-width="1.6"/></svg></div>
  <div class="abs" style="left:266px;top:196px;width:110px"><div class="label" style="font-size:8px">Nulla Facilisi In Et</div><p class="tiny">Praesent aliquet lorem ex, eu dapibus odio varius at. Duis eget tellus porta, consequat lacus vitae.</p></div>
  <div class="tile tile--dark" style="left:388px;top:198px"><svg viewBox="0 0 16 16"><path d="M3 13l4-6 3 3 4-6" fill="none" stroke="#fff" stroke-width="2"/></svg></div>
  <div class="abs" style="left:431px;top:196px;width:110px"><div class="label-ink" style="font-size:8px">Gravida Sit Amet Risus</div><p class="tiny">Praesent aliquet lorem ex, eu dapibus odio varius at. Duis eget tellus porta, consequat lacus vitae.</p></div>
  <div class="foot"><span class="foot-brand"><i></i>Stride Joint</span><div class="foot-bar">© 2022 Copyright Stride Joint Clinic - All Rights Reserved &nbsp;|&nbsp; 5</div></div>
</article>

<!-- 6 Three columns -->
<article class="slide col-b row-3">
  <h2 class="heading">Heading <span>Goes Here</span></h2>
  <div class="abs" style="left:0;top:75px;width:562px;height:42px;background:var(--teal);padding:9px 38px;text-align:center"><p class="tiny-w">Lorem ipsum dolor sit amet, consectetur adipiscing elit. Vivamus eu dui ex. Curabitur dapibus dignissim dui, in molestie metus feugiat sed. Praesent aliquet lorem ex, eu dapibus odio varius at. Duis eget tellus porta, consequat lacus vitae, venenatis dolor. Nulla facilisi. In et sollicitudin lacus. Donec risus orci, gravida sit amet risus vehicula, aliquet pretium sapien. Nullam sit amet magna non ex bibendum mollis. Nunc vel neque eu augue dignissim congue vitae magna.</p></div>
  <div class="abs" style="left:18px;top:142px;width:175px;text-align:center">
    <div style="width:34px;height:34px;background:var(--teal);margin:0 auto 10px"></div>
    <div class="label-ink" style="font-size:9.5px;margin-bottom:4px">Lorem Ipsum Dolor</div>
    <p class="tiny">Lorem ipsum dolor sit amet, consectetur adipiscing elit. Vivamus eu dui ex. Curabitur dapibus dignissim dui, in molestie metus feugiat sed. Praesent aliquet lorem ex, eu dapibus odio varius at. Duis eget tellus porta, consequat lacus vitae, venenatis dolor.</p>
  </div>
  <div class="abs" style="left:193px;top:142px;width:175px;text-align:center">
    <div style="width:34px;height:34px;background:var(--teal);margin:0 auto 10px"></div>
    <div class="label-ink" style="font-size:9.5px;margin-bottom:4px">Consequat Lacus Vitae</div>
    <p class="tiny">Lorem ipsum dolor sit amet, consectetur adipiscing elit. Vivamus eu dui ex. Curabitur dapibus dignissim dui, in molestie metus feugiat sed. Praesent aliquet lorem ex, eu dapibus odio varius at. Duis eget tellus porta, consequat lacus vitae, venenatis dolor.</p>
  </div>
  <div class="abs" style="left:368px;top:142px;width:175px;text-align:center">
    <div style="width:34px;height:34px;background:var(--teal);margin:0 auto 10px"></div>
    <div class="label-ink" style="font-size:9.5px;margin-bottom:4px">Bibendum Mollis</div>
    <p class="tiny">Lorem ipsum dolor sit amet, consectetur adipiscing elit. Vivamus eu dui ex. Curabitur dapibus dignissim dui, in molestie metus feugiat sed. Praesent aliquet lorem ex, eu dapibus odio varius at. Duis eget tellus porta, consequat lacus vitae, venenatis dolor.</p>
  </div>
  <div class="foot"><span class="foot-brand"><i></i>Stride Joint</span><div class="foot-bar">© 2022 Copyright Stride Joint Clinic - All Rights Reserved &nbsp;|&nbsp; 6</div></div>
</article>

<!-- 7 Numbered steps -->
<article class="slide col-a row-4">
  <div class="abs" style="left:361px;top:0;width:201px;height:189px;background:var(--teal)"></div>
  <div class="abs" style="left:44px;top:38px">
    <div class="kicker">ADIPISCING:</div>
    <div class="kicker-line">Elit Vivamus Eu Dui<br>Ex Curabitur</div>
  </div>
  <p class="abs" style="left:44px;top:140px;width:214px;font-size:6.4px;line-height:7.4px">Lorem ipsum dolor sit amet, consectetur adipiscing elit. Vivamus eu dui ex. Curabitur dapibus dignissim dui, in molestie metus feugiat sed. Praesent aliquet lorem ex, eu dapibus odio varius at. Duis eget tellus porta, consequat lacus vitae, venenatis dolor. Nulla facilisi. In et sollicitudin lacus. Donec risus orci, gravida sit amet risus vehicula, aliquet pretium sapien. Nullam sit amet magna non ex bibendum mollis. Nunc vel neque eu augue dignissim congue ut vitae magna. Phasellus eget commodo arcu. Nunc vitae semper dui. Integer venenatis, tellus sit amet interdum pretium, erat neque rhoncus turpis, a aliquam augue ligula eget erat.</p>
  <div class="num-card num-card--active" style="top:44px"><b>1</b><p>Lorem ipsum dolor sit amet, consectetur adipiscing elit. Vivamus eu dui ex. Curabitur dapibus dignissim dui, in molestie metus feugiat sed. Praesent aliquet lorem ex.</p></div>
  <div class="num-card" style="top:114px"><b>2</b><p>Lorem ipsum dolor sit amet, consectetur adipiscing elit. Vivamus eu dui ex. Curabitur dapibus dignissim dui, in molestie metus feugiat sed. Praesent aliquet lorem ex.</p></div>
  <div class="num-card" style="top:184px"><b>3</b><p>Lorem ipsum dolor sit amet, consectetur adipiscing elit. Vivamus eu dui ex. Curabitur dapibus dignissim dui, in molestie metus feugiat sed. Praesent aliquet lorem ex.</p></div>
  <div class="foot"><span class="foot-brand"><i></i>Stride Joint</span><div class="foot-bar">© 2022 Copyright Stride Joint Clinic - All Rights Reserved &nbsp;|&nbsp; 7</div></div>
</article>

<!-- 8 Chart -->
<article class="slide col-b row-4">
  <h2 class="heading">Heading <span>Goes Here</span></h2>
  <svg class="abs" style="left:45px;top:85px" width="290" height="115" viewBox="0 0 290 115">
    <defs>
      <linearGradient id="barA" x1="0" y1="0" x2="0" y2="1"><stop offset="0" stop-color="#5bb7b2"/><stop offset="1" stop-color="#8fd0cb"/></linearGradient>
      <linearGradient id="barB" x1="0" y1="0" x2="0" y2="1"><stop offset="0" stop-color="#2f7a75"/><stop offset="1" stop-color="#5bb7b2"/></linearGradient>
      <linearGradient id="barC" x1="0" y1="0" x2="0" y2="1"><stop offset="0" stop-color="#1f4f4c"/><stop offset="1" stop-color="#2f7a75"/></linearGradient>
    </defs>
    <g font-size="5.5" fill="#555" font-family="Ubuntu, sans-serif" text-anchor="end">
      <text x="8" y="8">6</text><text x="8" y="24">5</text><text x="8" y="40">4</text><text x="8" y="56">3</text><text x="8" y="72">2</text><text x="8" y="88">1</text><text x="8" y="104">0</text>
    </g>
    <line x1="12" y1="102" x2="280" y2="102" stroke="#ccc" stroke-width=".6"/>
    <rect x="20" y="33" width="14" height="69" fill="url(#barA)"/><rect x="37" y="64" width="14" height="38" fill="url(#barB)"/><rect x="54" y="70" width="14" height="32" fill="url(#barC)"/>
    <rect x="86" y="62" width="14" height="40" fill="url(#barA)"/><rect x="103" y="32" width="14" height="70" fill="url(#barB)"/><rect x="120" y="70" width="14" height="32" fill="url(#barC)"/>
    <rect x="152" y="46" width="14" height="56" fill="url(#barA)"/><rect x="169" y="73" width="14" height="29" fill="url(#barB)"/><rect x="186" y="54" width="14" height="48" fill="url(#barC)"/>
    <rect x="218" y="30" width="14" height="72" fill="url(#barA)"/><rect x="235" y="57" width="14" height="45" fill="url(#barB)"/><rect x="252" y="22" width="14" height="80" fill="url(#barC)"/>
    <g font-size="5.5" fill="#555" font-family="Ubuntu, sans-serif" text-anchor="middle">
      <text x="44" y="112">Category 1</text><text x="110" y="112">Category 2</text><text x="176" y="112">Category 3</text><text x="242" y="112">Category 4</text>
    </g>
  </svg>
  <p class="abs" style="left:48px;top:218px;width:280px" class="tiny"><span class="tiny" style="display:block">Lorem ipsum dolor sit amet, consectetur adipiscing elit. Vivamus eu dui ex. Curabitur dapibus dignissim dui, in molestie metus feugiat sed. Praesent aliquet lorem ex, eu dapibus odio varius at. Lorem ipsum dolor sit amet, consectetur adipiscing elit. Vivamus eu dui ex. Curabitur dapibus dignissim dui, in molestie metus feugiat sed. Praesent aliquet lorem ex, eu dapibus odio varius at.</span></p>
  <div class="abs" style="left:344px;top:85px;width:1px;height:180px;background:#ccc"></div>
  <div class="abs" style="left:360px;top:83px;width:160px">
    <div class="label" style="font-size:8px;display:flex;align-items:center;gap:6px"><i style="width:9px;height:9px;background:var(--teal);display:block"></i>Elit Vivamus Eu Dui Ex</div>
    <p class="tiny" style="padding-left:15px;margin:4px 0 20px">Lorem ipsum dolor sit amet, consectetur adipiscing elit. Vivamus eu dui ex. Curabitur dapibus dignissim dui, in molestie metus feugiat sed.</p>
    <div class="label" style="font-size:8px;display:flex;align-items:center;gap:6px;color:var(--teal-dark)"><i style="width:9px;height:9px;background:var(--teal-dark);display:block"></i>Donec risus orci, gravida sit</div>
    <p class="tiny" style="padding-left:15px;margin:4px 0 20px">Lorem ipsum dolor sit amet, consectetur adipiscing elit. Vivamus eu dui ex. Curabitur dapibus dignissim dui, in molestie metus feugiat sed.</p>
    <div class="label-ink" style="font-size:8px;display:flex;align-items:center;gap:6px"><i style="width:9px;height:9px;background:var(--ink);display:block"></i>Lorem ipsum dolor sit amet</div>
    <p class="tiny" style="padding-left:15px;margin-top:4px">Lorem ipsum dolor sit amet, consectetur adipiscing elit. Vivamus eu dui ex. Curabitur dapibus dignissim dui, in molestie metus feugiat sed.</p>
  </div>
  <div class="foot"><span class="foot-brand"><i></i>Stride Joint</span><div class="foot-bar">© 2022 Copyright Stride Joint Clinic - All Rights Reserved &nbsp;|&nbsp; 8</div></div>
</article>

<!-- 9 Table -->
<article class="slide col-a row-5">
  <h2 class="heading">Heading <span>Goes Here</span></h2>
  <table class="data">
    <thead><tr><th class="h0" style="width:156px">Heading Goes Here</th><th class="h1">Heading<br>Goes Here</th><th class="h2">Heading<br>Goes Here</th><th class="h3">Heading<br>Goes Here</th><th class="h4">Heading<br>Goes Here</th></tr></thead>
    <tbody>
      <tr><td>Lorem ipsum dolor sit amet</td><td>23</td><td>12</td><td>78</td><td>78</td></tr>
      <tr><td>Vivamus eu dui ex. Curabitur dapibus</td><td>45</td><td>56</td><td>12</td><td>76</td></tr>
      <tr><td>Praesent aliquet lorem ex, eu dapibus</td><td>78</td><td>76</td><td>34</td><td>34</td></tr>
      <tr><td>Duis eget tellus porta, consequat lacus</td><td>22</td><td>12</td><td>55</td><td>67</td></tr>
      <tr><td>Donec risus orci, gravida sit amet</td><td>34</td><td>66</td><td>45</td><td>11</td></tr>
      <tr><td>Nunc placerat, arcu nec mattis</td><td>67</td><td>47</td><td>78</td><td>23</td></tr>
      <tr><td>Nam semper tristique mauris</td><td>87</td><td>67</td><td>12</td><td>45</td></tr>
    </tbody>
  </table>
  <div class="col-frame"></div>
  <div class="foot"><span class="foot-brand"><i></i>Stride Joint</span><div class="foot-bar">© 2022 Copyright Stride Joint Clinic - All Rights Reserved &nbsp;|&nbsp; 9</div></div>
</article>

<!-- 10 Contact -->
<article class="slide cover col-b row-5">
  <div class="cover-panel"></div>
  <div class="brand brand--cover" style="top:123px">Stride Joint Clinic</div>
  <div class="abs" style="left:45px;top:165px;color:#fff;font-size:11px">Contact Us</div>
  <p class="abs tiny-w" style="left:45px;top:182px;width:150px">Lorem ipsum dolor sit amet, consectetur adipiscing elit. Vivamus eu dui ex.</p>
  <div class="abs" style="left:45px;top:202px;display:flex;flex-direction:column;gap:5px">
    <div class="tiny-w" style="display:flex;align-items:center;gap:6px"><svg width="8" height="8" viewBox="0 0 16 16"><path d="M3 2l3 0 1 4-2 1c1 2 2 3 4 4l1-2 4 1v3c0 1-1 1-1 1C7 14 2 9 2 3c0 0 0-1 1-1z" fill="#fff"/></svg>Lorem ipsum dolor sit amet, consectetur</div>
    <div class="tiny-w" style="display:flex;align-items:center;gap:6px"><svg width="8" height="8" viewBox="0 0 16 16"><circle cx="8" cy="8" r="6" fill="none" stroke="#fff" stroke-width="2"/><circle cx="8" cy="8" r="2" fill="#fff"/></svg>Curabitur dapibus dignissim dui</div>
    <div class="tiny-w" style="display:flex;align-items:center;gap:6px"><svg width="8" height="8" viewBox="0 0 16 16"><circle cx="8" cy="8" r="6" fill="none" stroke="#fff" stroke-width="1.5"/><path d="M2 8h12M8 2c-3 4-3 8 0 12M8 2c3 4 3 8 0 12" fill="none" stroke="#fff" stroke-width="1.2"/></svg>Donec risus orci, gravida sit amet risus vehicula</div>
  </div>
  <p class="cover-copy">© 2022 Copyright Stride Joint Clinic - All Rights Reserved</p>
</article>

</body>
</html>
```